Wellness Coach needs a Business Card

I need a business card for a start-up coaching business called Brightfern Vitality Partners. I don't have a logo as such but I am looking to have a web page created in a few months time and hopefully the person who designs this card will be able to do or help with the web project. This business card will be used primarily for networking and for initial clients.

As the name implies, the coaching focus is wide-ranging and includes multiple facets of health and wellness, including physical, mental, spiritual, etc. I am a Personal Trainer so the main focus will be physical training, but with the other areas of life / wellness included.

My information for the card:

Dorian Pleshey
Director
Brightfern Vitality Partners

Phone: 0413 862051
Address: PO Box 514 Mitchell ACT 2911
email: dorian@brightfernvitalitypartners.com.au
web: http://www.brightfernvitalitypartners.com.au

Target Market(s)

People wanting to change their life by getting fit and by addressing issues in their lives that are holding them back. I will target people already into fitness but who want to extend their approach into life coaching.

Industry/Entity Type

Health

Requirements
Must have
• - I am keen on a single sided business card design but if your design lends itself to a double sided design then I'm open to that thanks.

- I love the idea of fresh - something that represents the awakening of somebody who has been dormant. Lime green strikes me as fresh, but this is just an idea, not mandatory.
Nice to have
• - I'm keen for minimisation but I don't mind an image in the background taking up the whole space, as long as it is not too busy.

- Two types of images that I can visualise are a mountain summit or a path leading into nature or up a mountain - an adventure! Again, not mandatory, just an idea.
Should not have
• - I'm not keen on over-crowding.
- One image I'm not keen on is someone standing on top of a mountain with their arms in the air - too cliché.

```html
<!DOCTYPE html>
<html lang="en">
<head>
<meta charset="utf-8">
<title>Brightfern Vitality Partners – Business Card</title>
<link rel="stylesheet" href="https://fonts.googleapis.com/css2?family=Nunito:wght@500;600&family=Quicksand:wght@400;500;600&display=swap">
<style>
  :root {
    --page-bg: #ecebe8;
    --lime: #8cc63f;
    --lime-light: #a4d65e;
    --lime-dark: #7ab52f;
    --sky: #29a8e0;
    --ink: #6d6e71;
    --ink-soft: #8a8b8e;
    --card-white: #ffffff;
  }
  * { box-sizing: border-box; margin: 0; padding: 0; }
  html, body {
    width: 1200px; height: 1184px; overflow: hidden;
    background: var(--page-bg);
  }
  .sheet {
    position: relative; width: 1200px; height: 1184px;
  }
  .card {
    position: absolute; left: 170px; width: 860px; height: 491px;
    box-shadow: 0 10px 28px rgba(0,0,0,.18);
  }

  /* Front */
  .card-front {
    top: 70px;
    background: linear-gradient(110deg, var(--lime-dark) 0%, var(--lime) 45%, var(--lime-light) 100%);
    display: flex; align-items: center; padding-left: 90px; gap: 40px;
  }
  .front-mark {
    width: 160px; height: 160px; border-radius: 50%;
    border: 5px solid #fff; flex: none;
  }
  .front-name {
    font-family: "Nunito", sans-serif; font-weight: 600;
    font-size: 44px; line-height: 1.18; color: #fff;
    max-width: 460px;
  }

  /* Back */
  .card-back {
    top: 621px; background: var(--card-white);
    display: flex;
  }
  .back-brand {
    width: 480px; display: flex; flex-direction: column;
    align-items: center; justify-content: center; gap: 26px;
  }
  .back-mark {
    width: 120px; height: 120px; border-radius: 50%;
    border: 5px solid var(--lime);
  }
  .back-name {
    font-family: "Nunito", sans-serif; font-weight: 600;
    font-size: 30px; color: var(--lime);
  }
  .divider {
    width: 2px; background: var(--lime); margin: 50px 0;
  }
  .contact {
    flex: 1; padding: 58px 30px 0 42px;
    font-family: "Quicksand", sans-serif; color: var(--ink);
  }
  .person {
    font-family: "Quicksand", sans-serif; font-weight: 600;
    font-size: 30px; letter-spacing: 1px; text-transform: uppercase;
  }
  .person .first { color: var(--lime); }
  .person .last { color: var(--sky); }
  .role {
    font-size: 14px; text-transform: uppercase; letter-spacing: 1.5px;
    line-height: 1.4; margin-top: 4px; color: var(--ink-soft);
  }
  .details { list-style: none; margin-top: 62px; }
  .details li {
    display: flex; align-items: center; gap: 16px;
    font-size: 15px; font-weight: 500; margin-bottom: 14px;
  }
  .details li.address { margin-bottom: 42px; }
  .details svg { width: 18px; height: 18px; flex: none; fill: var(--sky); }
</style>
</head>
<body>
<main class="sheet">

  <section class="card card-front" aria-label="Card front">
    <div class="front-mark"></div>
    <div class="front-name">Brightfern Vitality Partners</div>
  </section>

  <section class="card card-back" aria-label="Card back">
    <div class="back-brand">
      <div class="back-mark"></div>
      <div class="back-name">Brightfern Vitality Partners</div>
    </div>
    <div class="divider"></div>
    <div class="contact">
      <h1 class="person"><span class="first">Dorian</span> <span class="last">Pleshey</span></h1>
      <p class="role">Director<br>Brightfern Vitality Partners</p>
      <ul class="details">
        <li class="address">
          <svg viewBox="0 0 24 24" aria-hidden="true"><path d="M12 2a7 7 0 0 0-7 7c0 5 7 13 7 13s7-8 7-13a7 7 0 0 0-7-7zm0 9.5A2.5 2.5 0 1 1 12 6.5a2.5 2.5 0 0 1 0 5z"/></svg>
          PO Box 514 Mitchell ACT 2911
        </li>
        <li>
          <svg viewBox="0 0 24 24" aria-hidden="true"><path d="M7 1h10a2 2 0 0 1 2 2v18a2 2 0 0 1-2 2H7a2 2 0 0 1-2-2V3a2 2 0 0 1 2-2zm0 3v14h10V4H7zm5 15.5a1 1 0 1 0 0 2 1 1 0 0 0 0-2z"/></svg>
          0413 862051
        </li>
        <li>
          <svg viewBox="0 0 24 24" aria-hidden="true"><path d="M2 5h20v14H2V5zm2 2v.4l8 5.3 8-5.3V7H4zm16 2.8-8 5.3-8-5.3V17h16V9.8z"/></svg>
          dorian@brightfernvitalitypartners.com.au
        </li>
        <li>
          <svg viewBox="0 0 24 24" aria-hidden="true"><path d="M12 2a10 10 0 1 0 0 20 10 10 0 0 0 0-20zm6.9 9h-3a15 15 0 0 0-1.3-5.6A8 8 0 0 1 18.9 11zM12 4.1c.9 1.2 1.8 3.6 2 6.9h-4c.2-3.3 1.1-5.7 2-6.9zM9.4 5.4A15 15 0 0 0 8.1 11h-3a8 8 0 0 1 4.3-5.6zM5.1 13h3a15 15 0 0 0 1.3 5.6A8 8 0 0 1 5.1 13zm6.9 6.9c-.9-1.2-1.8-3.6-2-6.9h4c-.2 3.3-1.1 5.7-2 6.9zm2.6-1.3a15 15 0 0 0 1.3-5.6h3a8 8 0 0 1-4.3 5.6z"/></svg>
          www.brightfernvitalitypartners.com.au
        </li>
      </ul>
    </div>
  </section>

</main>
</body>
</html>
```